Technology solutions catalog

Were looking for a catalogue to supplement our website and corporate branding.

Our website will give you a good understanding of our products and services as well as our theme.

Our base colour and logo is red, white and grey.

www.voltrane.com.au

The aim of the catalogue is to showcase our business IT services & solutions. This will be a mix of education about the new solutions available to small and medium business today and how these solutions can increase productivity.

We would also like tip sections

This isn't all about selling but also about educating SMB's of the new and exciting IT solutions available today and having them book a free consult with us to discuss further about how we can help the business.

Solutions and area's that the catalogue will need to cover include

Front Cover -
-About us section, with our business contact information (1st page)
- Introduction. (2nd page)
-Communication Solutions - this includes Email, IP phones and business IT networks (2 pages)
- Data & Storage solutions (2 pages)
- Hardware (1 pages)
- Business IT health check list (1 page)
- Services and support offering (2 pages)
- Software & Popular cloud solutions (2 pages)
- Website / E-commerce solutions (2 pages)
Back cover

Based on two pages per solution the whole catalogue will be around 14 pages.

We don't need any text content done. We would like Headings on pages including page numbers. Footer please.

We're looking for a template that we can have our designer finish off by adding in some further product and service image and text.

Thank you for your consideration

Target Market(s)

IT for small and medium businesses

Industry/Entity Type

Supplement

Requirements
Must have
• Size A4
• Design supplied in Adobe indesign so we can edit and add our text and content
• Clean design

```html
<!DOCTYPE html>
<html lang="en">
<head>
<meta charset="utf-8">
<title>Voltrane Catalogue – Communication Solutions</title>
<link rel="stylesheet" href="https://fonts.googleapis.com/css2?family=Open+Sans:wght@300;400;600;700&display=swap">
<style>
  :root {
    --backdrop: #e6e6e6;
    --paper: #ffffff;
    --paper-shade: #f1f1f1;
    --brand-red: #c8454f;
    --ink: #3a3a3a;
    --ink-soft: #8a8a8a;
    --folio: #4a4a4a;
    --accent-yellow: #e3df3e;
    --glass: rgba(255, 255, 255, 0.16);
    --glass-edge: rgba(255, 255, 255, 0.28);
    --glass-text: #ffffff;
  }
  * { box-sizing: border-box; margin: 0; padding: 0; }
  html, body {
    width: 1200px; height: 849px; overflow: hidden;
    background: var(--backdrop);
    font-family: "Open Sans", Arial, sans-serif;
  }
  .spread {
    position: absolute; left: 60px; top: 225px;
    width: 1080px; height: 400px;
    display: flex;
    box-shadow: 0 10px 24px rgba(0,0,0,0.18);
  }
  .page { position: relative; width: 540px; height: 400px; overflow: hidden; }

  /* Left page */
  .page--network .page__photo {
    position: absolute; inset: 0;
    background: linear-gradient(115deg, #d8cbb8 0%, #a27a58 30%, #b8683a 55%, #8c4a2a 78%, #5e3420 100%);
  }
  .glass-panel {
    position: absolute; left: 268px; width: 240px;
    background: var(--glass);
    border: 1px solid var(--glass-edge);
    color: var(--glass-text);
    padding: 10px 12px;
  }
  .glass-panel--email { top: 26px; height: 84px; }
  .glass-panel--network { top: 122px; height: 232px; }
  .glass-panel__title { font-weight: 300; font-size: 19px; line-height: 1.1; margin-bottom: 5px; }
  .glass-panel p { font-size: 6.8px; line-height: 1.45; margin-bottom: 6px; }
  .glass-panel__subtitle { font-weight: 600; font-size: 9px; margin: 8px 0 4px; }
  .service-list { list-style: none; font-size: 6.8px; line-height: 1.6; }
  .service-list li::before { content: ""; display: inline-block; width: 4px; height: 4px; background: var(--glass-text); margin-right: 5px; vertical-align: middle; }

  /* Right page */
  .page--phones { background: linear-gradient(90deg, var(--paper) 60%, var(--paper-shade)); display: flex; }
  .page__feature-image { width: 165px; height: 100%; background: var(--accent-yellow); flex: none; }
  .page__content { padding: 42px 26px 0 24px; color: var(--ink); }
  .page__title { color: var(--brand-red); font-weight: 400; font-size: 20px; margin-bottom: 8px; }
  .page__lead { font-weight: 700; font-size: 9px; margin-bottom: 7px; }
  .page__content p { font-size: 6.8px; line-height: 1.5; color: var(--ink-soft); margin-bottom: 7px; }
  .page__question { font-weight: 700; font-size: 9px; margin: 14px 0 7px; }
  .bullet-list { list-style: none; font-size: 6.8px; line-height: 1.5; color: var(--ink-soft); }
  .bullet-list li { position: relative; padding-left: 10px; margin-bottom: 5px; }
  .bullet-list li::before { content: ""; position: absolute; left: 0; top: 4px; width: 4px; height: 4px; background: var(--ink-soft); border-radius: 50%; }

  .folio {
    position: absolute; bottom: 14px; width: 14px; height: 14px;
    background: var(--folio); color: #fff;
    font-size: 7px; line-height: 14px; text-align: center;
  }
  .folio--left { left: 256px; }
  .folio--right { right: 14px; }
</style>
</head>
<body>
  <main class="spread">
    <section class="page page--network">
      <div class="page__photo" role="img" aria-label="Photo of a tablet point-of-sale terminal on a stand on a café counter, warm blurred background"></div>

      <article class="glass-panel glass-panel--email">
        <h2 class="glass-panel__title">Includes Email</h2>
        <p>Cloudwork Apps is a cloud-based productivity suite that helps you and your team connect and get work done from anywhere on any device. It's simple to use and manage, allowing you to work smarter and focus on what really matters.</p>
      </article>

      <article class="glass-panel glass-panel--network">
        <h2 class="glass-panel__title">Business Network</h2>
        <p>Having a secure, fast and reliable business network is imperative for all your connected devices to work for you.</p>
        <p>Your business network is the backbone of your Technology allowing your team and customers to connect to data and services at the office or on the road.</p>
        <p>At Voltrane we offer a range of network services, from consulting on your network requirements to implementation and support.</p>
        <h3 class="glass-panel__subtitle">Network Services</h3>
        <ul class="service-list">
          <li>Network consulting</li>
          <li>Managed networks</li>
          <li>Private IP networks</li>
          <li>Remote Access</li>
          <li>Virtual private networks</li>
        </ul>
      </article>

      <span class="folio folio--left">4</span>
    </section>

    <section class="page page--phones">
      <div class="page__feature-image" role="img" aria-label="Photo of a black corded telephone handset hanging against a yellow wall"></div>
      <div class="page__content">
        <h2 class="page__title">Office Phones</h2>
        <h3 class="page__lead">Big business phones at small business prices</h3>
        <p>Voltrane's digital office phone's are designed for small businesses and deliver the features of a traditional high-end PBX at a fraction of the price.</p>
        <p>You don't need any PBX hardware onsite – all you require are IP enabled handsets, a router and a suitable broadband connection. We provide you with everything you require to get up and running including setup and support.</p>
        <h3 class="page__question">Is Voltrane's Business PBX the right solution for me?</h3>
        <p>Voltrane's digital office phones are an appropriate solution where:</p>
        <ul class="bullet-list">
          <li>Your business is geographically dispersed but wishes to appear as one unified organisation with central or multiple call management/monitoring points.</li>
          <li>Your business wishes to use IP telephony without significant investment in hardware, software and technical support.</li>
          <li>You require a flexible phone system that provides staff with the ability to relocate quickly and seamlessly between offices, home, interstate and overseas without disruption.</li>
        </ul>
      </div>
      <span class="folio folio--right">5</span>
    </section>
  </main>
</body>
</html>
```